Pecan Ridge Paving. Chip Seal Done Right

I need my card to have all my basic information on it. Keep it simple. Include web site, phone number and email address. Include phrase Chip Seal Done Right or Pecan Ridge’s Top Paving Company. Keep card simple. Include color and logo. Put all contact info on card. Make card simple and not complicated.

Here is infuriation yo out in business card

Dale R. Whitmore
830.555.0173 cell phone
Dalewhitmore7@mailbarn.net
www.pecanridgepaving.net

Target Market(s)

Hill Country Texas USA

Industry/Entity Type

Road chip seal

Contact Information for Business Card

We chip seal roads for ranches and property owners

Font styles to use
Serif
Sans Serif
Decorative
Script

Colors
0054AA
0677BA
7BADD7
CADEEF
E8F1F8
EB3D1F
EC4F4E
F09395
F8D3D4
FCEDEE

Requirements
Must have
• Keep it simply
Nice to have
• Logo and all basic info

```html
<!DOCTYPE html>
<html lang="en">
<head>
<meta charset="UTF-8">
<title>Pecan Ridge Paving – Business Card</title>
<link href="https://fonts.googleapis.com/css2?family=Montserrat:wght@400;500;700;800&display=swap" rel="stylesheet">
<style>
  :root {
    --navy: #1c2a5e;
    --red: #b8202f;
    --grey: #5b5f68;
    --paper: #ffffff;
    --backdrop: #e9ebef;
  }
  * { box-sizing: border-box; margin: 0; padding: 0; }
  html, body { width: 1200px; height: 800px; overflow: hidden; }
  body {
    background: var(--backdrop);
    font-family: "Montserrat", Arial, sans-serif;
    display: flex;
    align-items: center;
    justify-content: center;
    gap: 60px;
  }
  .card {
    position: relative;
    width: 525px;
    height: 300px;
    background: var(--paper);
    overflow: hidden;
    box-shadow: 0 6px 18px rgba(0,0,0,.12);
  }
  /* shared decorative disc */
  .card-disc {
    position: absolute;
    border-radius: 50%;
    background: var(--navy);
  }
  .card--front .card-disc { width: 260px; height: 260px; right: -70px; top: -120px; }
  .card--back  .card-disc { width: 300px; height: 300px; left: -170px; top: 10px; }

  /* front */
  .holder {
    position: absolute; left: 34px; top: 40px;
    font-size: 15px; color: var(--grey); font-weight: 500;
  }
  .holder-name { color: var(--red); font-weight: 700; letter-spacing: .5px; }
  .holder-sep { color: var(--red); margin: 0 4px; }
  .contact-list { position: absolute; left: 34px; top: 78px; list-style: none; }
  .contact-list li {
    display: flex; align-items: center; gap: 9px;
    font-size: 13.5px; color: var(--grey); margin-bottom: 7px;
  }
  .contact-list svg { width: 13px; height: 13px; fill: var(--navy); flex: none; }
  .rule {
    position: absolute; left: 34px; right: 120px; top: 196px;
    height: 1px; background: var(--red);
  }
  .brand { position: absolute; display: flex; flex-direction: column; }
  .brand-name {
    font-weight: 800; color: var(--navy); text-transform: uppercase;
    line-height: 1.05; letter-spacing: .3px;
  }
  .brand-tag {
    font-size: 8px; color: var(--red); letter-spacing: 1px; margin-top: 5px;
    font-weight: 500; align-self: flex-end;
  }
  .card--front .brand { left: 34px; top: 214px; }
  .card--front .brand-name { font-size: 24px; }
  .card--back .brand { right: 48px; top: 108px; }
  .card--back .brand-name { font-size: 28px; }
  .brand-row { display: flex; align-items: center; gap: 10px; }
  .brand-dot { width: 26px; height: 26px; border-radius: 50%; background: var(--red); flex: none; }
</style>
</head>
<body>

<section class="card card--front" aria-label="Business card front">
  <div class="card-disc"></div>
  <p class="holder"><span class="holder-name">JOHN DOE</span><span class="holder-sep">|</span>Director</p>
  <ul class="contact-list">
    <li><svg viewBox="0 0 24 24"><path d="M6.6 10.8a15.1 15.1 0 0 0 6.6 6.6l2.2-2.2a1 1 0 0 1 1-.25 11.4 11.4 0 0 0 3.6.57 1 1 0 0 1 1 1V20a1 1 0 0 1-1 1A17 17 0 0 1 3 4a1 1 0 0 1 1-1h3.5a1 1 0 0 1 1 1c0 1.25.2 2.45.57 3.6a1 1 0 0 1-.25 1z"/></svg>(00) 0000 0000</li>
    <li><svg viewBox="0 0 24 24"><path d="M2 5h20v14H2zm2 2v.5l8 5 8-5V7zm0 2.8V17h16V9.8l-8 5z"/></svg>info@pecanridgepaving.net</li>
    <li><svg viewBox="0 0 24 24"><path d="M12 2a10 10 0 1 0 0 20 10 10 0 0 0 0-20zm6.9 9h-3a15 15 0 0 0-1.3-6 8 8 0 0 1 4.3 6zM12 4c.9 1.2 1.8 3.7 1.9 7h-3.8C10.2 7.7 11.1 5.2 12 4zM9.4 5a15 15 0 0 0-1.3 6h-3a8 8 0 0 1 4.3-6zM5.1 13h3a15 15 0 0 0 1.3 6 8 8 0 0 1-4.3-6zm5 0h3.8c-.1 3.3-1 5.8-1.9 7-.9-1.2-1.8-3.7-1.9-7zm4.5 6a15 15 0 0 0 1.3-6h3a8 8 0 0 1-4.3 6z"/></svg>www.pecanridgepaving.net</li>
    <li><svg viewBox="0 0 24 24"><path d="M12 2a7 7 0 0 0-7 7c0 5 7 13 7 13s7-8 7-13a7 7 0 0 0-7-7zm0 9.5A2.5 2.5 0 1 1 12 6.5a2.5 2.5 0 0 1 0 5z"/></svg>12 dummy city, dummy place 0000</li>
  </ul>
  <div class="rule"></div>
  <div class="brand">
    <div class="brand-row"><span class="brand-dot"></span><span class="brand-name">Pecan Ridge Paving</span></div>
    <span class="brand-tag">OVER 40 YEARS</span>
  </div>
</section>

<section class="card card--back" aria-label="Business card back">
  <div class="card-disc"></div>
  <div class="brand">
    <div class="brand-row"><span class="brand-dot"></span><span class="brand-name">Pecan Ridge<br>Paving</span></div>
    <span class="brand-tag">OVER 40 YEARS</span>
  </div>
</section>

</body>
</html>
```